Small animal veterinary clinic needs a new web site design

We need a new web site design for Harlowe Veterinary Clinic. The clinic performs medicine, surgery, and wellness care for cats and dogs. We have been in business for over 50 years so we want to project stability, reliability, class, elegance, and professionalism. We also want to convey that we have modern facilities and services and perform high quality medicine.
The current web site has been in place for many years and looks stale but for reference it is at http://www.harlowevetcare.example. We will be re-writing most of the content and looking to add additional pages, videos, downloadable documents (forms, brochures, marketing materials, etc.) The new owners prefer a more classy, modern look. Some vet clinic sites we like are http://pintrelpaws.example and http://corvalanimalcare.example. We like a nice, clean, fresh, interactive interface.
Our new logo is attached. We want the color scheme of the web site to be complementary to the colors in the logo, especially the blue and green. The purple color of the text should just be used for accent. Upon request and if necessary, I can supply the Adobe Illustrator source file for the logo.
We are looking for a set of page designs - a great, eye-catching home page and 2-3 content page layouts we can use to create content pages with our own text and other content. Navigation design is very important as well. Again, we can fill in the content of the navigation links but I would like a nice, easy-to-use, logical navigation design. If you want some content or navigation links to use as reference during your design phase, feel free to pull whatever content or navigation you want from our existing web site. I am not looking for just images, I would like actual page files - HTML, CSS, etc.
Thanks and good luck!
Target Market(s)
We cater to pet owners across a wide age range. Socio-economic status of our customers is middle class and above. We do not target price shoppers.
Industry/Entity Type
Veterinary
Colors
Designer to choose colors to be used in the design.
Requirements
Must have
- Must look professional, clean, and modern. We are looking for simple but elegant design and navigation. 1 home page design, 2-3 content page designs delivered with code (HTML & CSS).
Nice to have
- When HTML/CSS is delivered, it would be awesome if it were mobile ready as well.
Should not have
- Colors that are too bold. Layout that is too complex.

```html
<!DOCTYPE html>
<html lang="en">
<head>
<meta charset="utf-8">
<title>Harlowe Veterinary Clinic</title>
<link href="https://fonts.googleapis.com/css2?family=Hind:wght@400;500;600;700&family=Arimo:wght@400&display=swap" rel="stylesheet">
<style>
:root{
  --teal:#2f8590;
  --teal-dark:#256f79;
  --teal-deep:#2a6e78;
  --navy:#1f5d8c;
  --title-teal:#2d7f88;
  --text:#5a5a5a;
  --line:#d4d8d9;
  --card:#f1f1f1;
  --white:#ffffff;
}
*{margin:0;padding:0;box-sizing:border-box}
html,body{width:913px;height:1200px;overflow:hidden;background:var(--white)}
body{position:relative;font-family:"Arimo",Arial,sans-serif;color:var(--text)}
.abs{position:absolute}
.head-font{font-family:"Hind",Arial,sans-serif}
.top-band{left:0;top:0;width:913px;height:6px;background:var(--teal-dark)}
.header-bg{left:0;top:6px;width:913px;height:120px;background:linear-gradient(#bfe0e0,#e9f4f4 70%,#fff)}
.logo{left:131px;top:12px;width:152px;height:152px;border-radius:50%;background:#fff;box-shadow:0 3px 6px rgba(0,0,0,.35);display:flex;align-items:center;justify-content:center;z-index:3}
.logo span{font-family:"Hind",sans-serif;font-weight:600;font-size:19px;color:var(--teal-deep);letter-spacing:.5px}
.signin-note{left:340px;top:30px;width:181px;text-align:right;font-family:"Hind",sans-serif;font-weight:500;font-size:11px;line-height:17px;color:#3b4b4e}
.btn-top{top:29px;height:29px;border-radius:4px;background:linear-gradient(var(--teal),var(--teal-dark));color:#fff;font-family:"Hind",sans-serif;font-weight:500;font-size:10px;display:flex;align-items:center;justify-content:center}
.main-nav{left:282px;top:78px;width:500px;height:30px;border-radius:0 4px 4px 0;background:linear-gradient(var(--teal),var(--teal-dark));display:flex;align-items:center;justify-content:space-around;padding-left:16px}
.main-nav a{color:#fff;text-decoration:none;font-family:"Hind",sans-serif;font-weight:500;font-size:9.5px}
.hero{left:130px;top:124px;width:652px;height:298px;border-radius:16px;overflow:hidden;background:linear-gradient(100deg,#6eaab0 0%,#a9cfd1 35%,#c9dfe0 55%,#3f9bc2 80%,#2a8fbf 100%)}
.hero-title{left:178px;top:186px;font-family:"Hind",sans-serif;font-weight:700;font-size:33px;color:#fff}
.hero-sub{left:178px;top:219px;font-family:"Hind",sans-serif;font-weight:700;font-size:22px;color:var(--title-teal)}
.hero-text{left:180px;top:256px;width:280px;font-family:"Hind",sans-serif;font-size:11px;line-height:20px;color:#3d4a4c}
.hero-btn{left:182px;top:327px;width:172px;height:36px;border-radius:5px;background:#f5f7f7;color:var(--navy);font-family:"Hind",sans-serif;font-weight:500;font-size:10px;display:flex;align-items:center;justify-content:center}
.hero-arrows{left:731px;top:394px;width:36px;height:18px;background:rgba(160,170,170,.45)}
.welcome-title{left:0;top:446px;width:913px;text-align:center;font-family:"Hind",sans-serif;font-weight:500;font-size:15px;color:var(--navy)}
.welcome-text{left:150px;top:478px;width:613px;text-align:center;font-size:9px;line-height:18px}
.divider{height:1px;background:var(--line)}
.section-title{font-family:"Hind",sans-serif;font-weight:500;font-size:12px;color:var(--navy)}
.pager{font-size:11px;color:#aaa;letter-spacing:4px}
.staff-card{top:593px;width:153px;height:211px;border:1px solid #dcdcdc;border-radius:10px;background:var(--card);overflow:hidden;text-align:center}
.staff-photo{position:absolute;left:46px;top:27px;width:61px;height:61px;border-radius:50%;background:linear-gradient(#7a8b7a,#3c463e)}
.staff-name{position:absolute;left:0;top:98px;width:100%;font-family:"Hind",sans-serif;font-weight:500;font-size:9px;line-height:16px;color:var(--navy)}
.staff-bio{position:absolute;left:8px;top:134px;width:137px;font-size:8px;line-height:15px;color:#6a6a6a}
.staff-more{position:absolute;left:0;bottom:0;width:100%;height:31px;background:var(--teal);color:#fff;font-family:"Hind",sans-serif;font-weight:600;font-size:8.5px;display:flex;align-items:center;justify-content:center}
.about-photo{left:494px;top:593px;width:288px;height:103px;border-radius:10px;background:linear-gradient(90deg,#d9c6b8,#efe9e2 45%,#c9d8e6 75%,#9cc2e8)}
.about-text{left:496px;top:706px;width:290px;font-size:8px;line-height:15px;color:#6a6a6a}
.about-btn{left:496px;top:779px;width:97px;height:23px;border-radius:3px;background:var(--teal);color:#fff;font-family:"Hind",sans-serif;font-weight:500;font-size:8.5px;display:flex;align-items:center;justify-content:center}
.news-item{top:896px;width:210px;height:64px}
.news-photo{position:absolute;left:0;top:0;width:64px;height:64px;border-radius:50%}
.news-title{position:absolute;left:76px;top:2px;font-family:"Hind",sans-serif;font-weight:500;font-size:10.5px;color:var(--navy)}
.news-date{position:absolute;left:77px;top:19px;font-size:8px;color:#555}
.news-text{position:absolute;left:76px;top:34px;width:140px;font-size:8px;line-height:15px;color:#6a6a6a}
.footer{left:0;top:1000px;width:913px;height:164px;background:var(--teal)}
.footer-bottom{left:0;top:1164px;width:913px;height:36px;background:var(--teal-dark);color:#fff;font-size:8px;display:flex;align-items:center;justify-content:center}
.foot-col{top:1020px;color:#fff;font-size:8px}
.foot-col h3{font-family:"Hind",sans-serif;font-weight:500;font-size:10px;padding-bottom:7px;border-bottom:1px solid rgba(255,255,255,.7);margin-bottom:8px;padding-left:2px}
.foot-col ul{list-style:none}
.foot-col li{line-height:16.3px;padding-left:2px}
.contact li{display:flex;align-items:flex-start;line-height:18px}
.contact svg{flex:none;margin:4px 8px 0 0}
.social li{display:flex;align-items:center;height:27px}
.social .dot{width:20px;height:20px;border-radius:50%;background:#fff;margin-right:4px}
</style>
</head>
<body>
<div class="abs header-bg"></div>
<div class="abs top-band"></div>

<div class="abs logo"><span>HARLOWE</span></div>
<div class="abs signin-note">SIGN-IN TO YOUR PERSONALIZED<br>PET PORTAL TODAY!</div>
<div class="abs btn-top" style="left:538px;width:73px">SIGN IN</div>
<div class="abs btn-top" style="left:618px;width:164px">REQUEST AN APPOINTMENT</div>
<nav class="abs main-nav">
  <a href="#">OUR PRACTICE</a><a href="#">SERVICES</a><a href="#">OUR STAFF</a><a href="#">CARE GUIDES</a><a href="#">CONTACT US</a><a href="#">MORE INFO</a>
</nav>

<div class="abs hero" role="img" aria-label="Smiling veterinarian in blue scrubs holding a small terrier"></div>
<div class="abs hero-title">HARLOWE</div>
<div class="abs hero-sub">VETERINARY CLINIC</div>
<p class="abs hero-text">&nbsp;The clinic performs medicine, surgery, and wellness care for cats and dogs. We have been in business for over 50 years</p>
<div class="abs hero-btn">CLICK HERE FOR MORE INFO</div>
<div class="abs hero-arrows"></div>

<h1 class="abs welcome-title">WELCOME TO HARLOWE</h1>
<p class="abs welcome-text">Harlowe Veterinary Clinic is a full-service veterinary medical hospital, located in Brookhaven, SC. The professional and courteous staff at Harlowe Veterinary Clinic seeks to provide the best possible medical care, surgical care and dental care for their highly-valued...</p>
<div class="abs divider" style="left:130px;top:534px;width:652px"></div>

<h2 class="abs section-title" style="left:130px;top:564px">OUR STAFFS</h2>
<div class="abs pager" style="left:434px;top:563px">‹ ›</div>
<div class="abs staff-card" style="left:130px">
  <div class="staff-photo" role="img" aria-label="Portrait of the clinic owner holding a spaniel"></div>
  <div class="staff-name">OWEN R. CALLOWAY, D.V.M.<br>OWNER / VETERINARIAN</div>
  <div class="staff-bio">Dr. Owen Calloway received his BS (with distinction)</div>
  <div class="staff-more">MORE ABOUT ME</div>
</div>
<div class="abs staff-card" style="left:300px">
  <div class="staff-photo" role="img" aria-label="Portrait of a veterinarian holding a small dog"></div>
  <div class="staff-name">MARLA T<br>WESTCOTT, D.V.M</div>
  <div class="staff-bio">Dr. Marla Westcott received her BS (cum laude) in Biology</div>
  <div class="staff-more">MORE ABOUT ME</div>
</div>

<h2 class="abs section-title" style="left:496px;top:564px">ABOUT HARLOWE</h2>
<div class="abs about-photo" role="img" aria-label="Pet owner and veterinarian with a labrador"></div>
<p class="abs about-text">Harlowe Veterinary Clinic is a full-service veterinary medical hospital, located in Brookhaven, SC. The professional and courteous staff at Harlowe Veterinary Clinic seeks to provide the best possible medical care, surgical care and dental care for their highly-valued...</p>
<div class="abs about-btn">READ MORE INFO</div>

<h2 class="abs section-title" style="left:130px;top:843px">LATEST NEWS</h2>
<div class="abs pager" style="left:762px;top:842px">‹ ›</div>
<div class="abs divider" style="left:130px;top:873px;width:652px"></div>

<div class="abs news-item" style="left:130px">
  <div class="news-photo" role="img" aria-label="Veterinarian examining a kitten" style="background:linear-gradient(#f1e6dc,#d9b48f)"></div>
  <div class="news-title">WE OFFER PET PORTALS!</div>
  <div class="news-date">Fri Mar 22 - 2013</div>
  <div class="news-text">Harlowe Veterinary Clinic is a full service veterinary medical...</div>
</div>
<div class="abs news-item" style="left:358px">
  <div class="news-photo" role="img" aria-label="Tabby cat resting" style="background:linear-gradient(#8c8378,#4a443d)"></div>
  <div class="news-title">WE OFFER PET PORTALS!</div>
  <div class="news-date">Fri Mar 22 - 2013</div>
  <div class="news-text">Harlowe Veterinary Clinic is a full service veterinary medical...</div>
</div>
<div class="abs news-item" style="left:586px">
  <div class="news-photo" role="img" aria-label="Corgi on a green lawn" style="background:linear-gradient(#b9cf86,#c98a4c)"></div>
  <div class="news-title">WE OFFER PET PORTALS!</div>
  <div class="news-date">Fri Mar 22 - 2013</div>
  <div class="news-text">Harlowe Veterinary Clinic is a full service veterinary medical...</div>
</div>

<footer>
<div class="abs footer"></div>
<div class="abs foot-col" style="left:138px;width:112px">
  <h3>WELCOME</h3>
  <ul><li>Our Practice</li><li>Services</li><li>Our Staff</li><li>Care Guides</li><li>Contact Us</li><li>More Info</li></ul>
</div>
<div class="abs foot-col contact" style="left:294px;width:112px">
  <h3>CONTACT</h3>
  <ul>
    <li><svg width="7" height="9" viewBox="0 0 7 9"><path d="M3.5 0a3.2 3.2 0 0 0-3.2 3.2C.3 5.6 3.5 9 3.5 9s3.2-3.4 3.2-5.8A3.2 3.2 0 0 0 3.5 0zm0 4.4a1.2 1.2 0 1 1 0-2.4 1.2 1.2 0 0 1 0 2.4z" fill="#fff"/></svg><span style="white-space:nowrap">2210 Alder Grove Road<br>Brookhaven, SC 29401</span></li>
    <li><svg width="7" height="9" viewBox="0 0 7 9"><rect x=".8" y=".5" width="5.4" height="8" rx="1" fill="none" stroke="#fff"/></svg>Phone: (555) 214-3870</li>
    <li><svg width="8" height="8" viewBox="0 0 8 8"><rect x="2" y="0" width="4" height="3" fill="#fff"/><rect x="0" y="3" width="8" height="3.5" fill="#fff"/><rect x="2" y="6" width="4" height="2" fill="#fff"/></svg>Fax: (555) 214-3871</li>
    <li style="white-space:nowrap"><svg width="9" height="7" viewBox="0 0 9 7"><rect width="9" height="7" fill="#fff"/><path d="M0 0l4.5 3.8L9 0" fill="none" stroke="#2f8590"/></svg>Email: hello@harlowevet.example</li>
  </ul>
</div>
<div class="abs foot-col" style="left:458px;width:154px">
  <h3>TIMINGS</h3>
  <ul><li>Mon-Fri: 8:00am - 5:30pm</li><li>Sat: 8:00am - 11:30am</li><li>Sun: Closed</li><li><u>After Hours Emergency:</u></li><li style="white-space:nowrap">Veterinary Emergency Care (555) 318-9064</li></ul>
</div>
<div class="abs foot-col social" style="left:664px;width:112px">
  <h3>SOCIAL NETWORK</h3>
  <ul><li><span class="dot"></span>: Friendbook</li><li><span class="dot"></span>: Chirper</li><li><span class="dot"></span>: Linkwork</li></ul>
</div>
<div class="abs footer-bottom">Copyright © 2014. Harlowe. All rights reserved.</div>
</footer>
</body>
</html>
```